Provocative psychotherapy with a difference (Corporate Design)

I'm a psychotherapist, job coach and communication trainer for courses in conflict management and team building. I workwith provocative therapy and paradoxical interventions, with hypnosis for single people, couples or groups. So id like the logo to be provocative, or display a paradox of some kind, fresh and creative, modern, shoulderstand stand for openness, be fresh but still having a professional touch to it. The logo shoulderstand catch the customers interest and curiosity but stopped for safety in a way of: here I can find out something about myself, here I can explore, here I can make a new experience.

Target Market(s)

I work with young adults, adults and companies With Their senior management. So a logo shoulderstand attract all Of Those customers.

Industry/Entity Type

Mental Health

Contact Information for Business Card

kurz drüben
Verena Kastholm
lic. phil. Psychologin FSP
Therapie, Coaching und Training
Wabernweg 382
8057 Zürich
Telefon +41 44 586 37 92
E-Mail verena.kastholm@postfeld.ch
Internet www.verenakastholm.ch oder www.kurzdrueben.ch

Logo Text

kurz drüben (Therapie . Coaching . Training)

Number of Pages Required

1 page

Logo styles of interest
Pictorial/Combination Logo
Abstract Logo
Wordmark Logo
Font styles to use
Sans Serif

Requirements
Must have
• Little color (max 3 colors). I like earthy colors, or gray shades, gold, turquoise or petrol (like the colors of my chair in the room)
Nice to have
• see description
Should not have
• Nogo: Red, orange or yellow colors

```html
<!DOCTYPE html>
<html lang="de">
<head>
<meta charset="utf-8">
<title>kurz drüben – Corporate Design</title>
<link rel="stylesheet" href="https://fonts.googleapis.com/css2?family=Exo+2:wght@400;500&family=Roboto+Condensed:wght@400;500&display=swap">
<style>
  :root {
    --canvas: #f6f5f3;
    --paper: #f3f3f3;
    --navy: #1e3a52;
    --blue: #0a93c7;
    --card-blue: #2ba3cf;
    --card-dark: #3d4d60;
    --card-dark-deep: #33414f;
    --muted: #6b7682;
    --white: #ffffff;
  }
  * { box-sizing: border-box; margin: 0; padding: 0; }
  html, body { width: 1200px; height: 1000px; overflow: hidden; }
  body {
    background: var(--canvas);
    font-family: "Exo 2", sans-serif;
    color: var(--navy);
    position: relative;
  }

  /* Letterhead */
  .letterhead {
    position: absolute; left: 60px; top: 50px;
    width: 520px; height: 735px;
    background: var(--paper);
    box-shadow: 0 2px 10px rgba(0,0,0,0.08);
  }
  .letterhead__brand { position: absolute; left: 70px; top: 70px; text-align: left; }
  .letterhead__name { font-size: 22px; font-weight: 400; color: var(--navy); display: flex; align-items: center; gap: 8px; }
  .brand-square { width: 12px; height: 12px; background: var(--blue); display: inline-block; }
  .letterhead__tagline {
    font-family: "Roboto Condensed", sans-serif; font-size: 6px; letter-spacing: 1.6px;
    color: var(--blue); margin-top: 4px; margin-left: 20px;
  }
  .letterhead__cta { position: absolute; left: 90px; top: 150px; font-size: 8px; color: var(--navy); }
  .letterhead__contact { position: absolute; right: 40px; bottom: 40px; width: 140px; }
  .letterhead__phone, .letterhead__address {
    font-size: 6px; letter-spacing: 1px; color: var(--muted);
  }
  .letterhead__address { margin-top: 6px; line-height: 1.5; }
  .letterhead__panel {
    background: var(--card-blue); height: 90px; margin-top: 4px;
    padding: 38px 0 0 18px; color: var(--white);
  }
  .letterhead__panel-name { font-size: 11px; }
  .letterhead__panel-tag { font-size: 4.5px; letter-spacing: 0.8px; margin-top: 2px; }

  /* Business cards */
  .card {
    position: absolute; top: 810px; width: 263px; height: 170px;
    box-shadow: 0 2px 8px rgba(0,0,0,0.15);
  }
  .card--back { left: 60px; background: linear-gradient(160deg, var(--card-dark), var(--card-dark-deep)); color: var(--white); }
  .card__cta { position: absolute; left: 22px; top: 78px; font-size: 9px; }
  .card__phone { position: absolute; left: 140px; top: 18px; font-size: 6px; letter-spacing: 1px; }
  .card__panel {
    position: absolute; left: 132px; top: 34px; width: 118px; height: 80px;
    background: var(--card-blue); padding: 30px 0 0 12px;
  }
  .card__panel-name { font-size: 11px; }
  .card__panel-tag { font-size: 4.5px; letter-spacing: 0.8px; margin-top: 2px; }
  .card__address { position: absolute; left: 140px; top: 124px; font-size: 6px; letter-spacing: 0.8px; line-height: 1.5; }

  .card--front { left: 340px; background: var(--card-blue); color: var(--white); padding: 60px 0 0 24px; }
  .card__name { font-size: 15px; }
  .card__role { font-size: 6px; letter-spacing: 0.8px; margin-top: 4px; }

  /* Brand block */
  .brand {
    position: absolute; left: 800px; top: 200px; width: 340px; text-align: center;
  }
  .brand__mark { display: flex; justify-content: center; align-items: center; gap: 16px; }
  .brand__name { font-size: 54px; font-weight: 400; color: var(--navy); letter-spacing: 0.5px; }
  .brand__square { width: 30px; height: 30px; background: var(--blue); }
  .brand__tagline {
    font-family: "Roboto Condensed", sans-serif; font-weight: 500;
    font-size: 12px; letter-spacing: 2.6px; color: var(--blue); margin-top: 22px;
  }
  .brand__cta {
    position: absolute; left: 800px; top: 512px; width: 340px; text-align: center;
    font-size: 22px; letter-spacing: 1.5px; color: var(--navy);
  }
</style>
</head>
<body>
  <section class="letterhead">
    <div class="letterhead__brand">
      <div class="letterhead__name"><span class="brand-square"></span>kurz drüben</div>
      <div class="letterhead__tagline">THERAPIE . COACHING . TRAINING</div>
    </div>
    <div class="letterhead__cta">eingehen &gt;</div>
    <div class="letterhead__contact">
      <div class="letterhead__phone">+41 44 586 37 92</div>
      <div class="letterhead__panel">
        <div class="letterhead__panel-name">kurz drüben</div>
        <div class="letterhead__panel-tag">therapie . coaching . training</div>
      </div>
      <div class="letterhead__address">Wabernweg 382<br>8057 Zürich</div>
    </div>
  </section>

  <section class="card card--back">
    <div class="card__cta">eingehen &gt;</div>
    <div class="card__phone">+41 44 586 37 92</div>
    <div class="card__panel">
      <div class="card__panel-name">kurz drüben</div>
      <div class="card__panel-tag">therapie . coaching . training</div>
    </div>
    <div class="card__address">Wabernweg 382<br>8057 Zürich</div>
  </section>

  <section class="card card--front">
    <div class="card__name">kurz drüben</div>
    <div class="card__role">therapie . coaching . training</div>
  </section>

  <section class="brand">
    <div class="brand__mark"><span class="brand__square"></span><span class="brand__name">kurz drüben</span></div>
    <div class="brand__tagline">THERAPIE . COACHING . TRAINING</div>
  </section>
  <div class="brand__cta">eingehen &gt;</div>
</body>
</html>
```